Missing Kids Car Doantion Website Design

Please create a new one page website design.

Current site: http://autosforyouth.net/

New WEBSITE address is: VansForLostYouth.org

Use these sites for an idea of what I am looking for. I like these sites best: tiresforsoldiers.org and autosforsoldiers.org

Coding

Coded - Design and coding required

Number of Pages Required

1 page

```html
<!DOCTYPE html>
<html lang="en">
<head>
<meta charset="utf-8">
<title>Autos For Youth – Donate Your Car</title>
<link rel="stylesheet" href="https://fonts.googleapis.com/css2?family=Lato:wght@400;700;900&family=Luckiest+Guy&family=Patrick+Hand&display=swap">
<style>
:root{
  --sky:#3aa9e6;
  --sky-light:#6cc6f2;
  --sky-pale:#d9f0fc;
  --pink:#f0245a;
  --orange:#f15a29;
  --green:#18a84a;
  --ink:#333a40;
  --muted:#5c6670;
  --white:#ffffff;
  --dark:#2b2b2b;
  --red:#e8222f;
}
*{margin:0;padding:0;box-sizing:border-box}
html,body{width:1200px;height:3651px;overflow:hidden}
body{position:relative;background:var(--white);font-family:"Lato",sans-serif;color:var(--ink)}
.abs{position:absolute}
.btn{position:absolute;display:flex;align-items:center;justify-content:center;background:var(--pink);color:var(--white);font:700 15px "Lato",sans-serif;text-transform:uppercase;border-radius:3px;letter-spacing:.3px;white-space:nowrap}
.tag{position:absolute;display:flex;align-items:center;justify-content:center;color:var(--white);font:400 34px "Patrick Hand",cursive;border-radius:6px;white-space:nowrap}
.tag.orange{background:var(--orange)}
.tag.green{background:var(--green)}

/* hero */
.hero{left:0;top:0;width:1200px;height:800px;background:linear-gradient(180deg,#2f9fe0 0%,#56bdf0 60%,#8fd6f7 100%)}
.nav{right:118px;top:32px;display:flex;gap:26px;font:700 15px "Lato",sans-serif;color:var(--white)}
.brand{left:183px;top:110px;width:352px;height:140px;background:var(--white);border-radius:10px;display:flex;align-items:center;justify-content:center;gap:14px;font:900 30px "Lato",sans-serif;color:var(--sky)}
.brand .dot{width:34px;height:34px;border-radius:50%;background:var(--sky)}
.headline{left:150px;top:276px;width:420px;text-align:center;font:400 54px/60px "Luckiest Guy",cursive;color:var(--white);white-space:nowrap}
.subhead{left:160px;top:342px;width:400px;text-align:center;font:700 30px/36px "Lato",sans-serif;color:var(--white);letter-spacing:.5px;white-space:nowrap}
.mini-brand{left:200px;top:405px;width:110px;text-align:center;font:700 13px "Lato",sans-serif;color:var(--white)}
.mini-brand .sq{display:block;width:34px;height:34px;margin:0 auto 6px;background:#f6d11d}
.perks{left:330px;top:405px;list-style:none;font:400 13px "Lato",sans-serif;color:var(--white);line-height:20px}
.form{left:694px;top:102px;width:382px;height:438px;background:rgba(255,255,255,.28);border-radius:4px;padding:22px 24px}
.form h2{font:400 29px "Patrick Hand",cursive;color:#1c4e9c}
.form p{font:400 13px "Lato",sans-serif;color:var(--pink);margin-bottom:14px}
.row{display:flex;gap:8px;margin-bottom:10px}
.field{flex:1;height:42px;background:var(--white);border:1px solid #cfe6f3;font:400 12px "Lato",sans-serif;color:#777;display:flex;align-items:center;justify-content:space-between;padding:0 10px}
.form .btn{position:static;height:48px;width:100%;font-size:17px;margin-top:6px}
.kids{left:304px;top:572px;width:596px;height:218px;background:linear-gradient(90deg,#f2c7a4,#e8a2b7,#f4d38a,#c9a7e0);border-radius:100px 100px 0 0}
.wave{left:0;top:700px}

/* missing kids */
.arrow-btn{width:27px;height:27px;border-radius:3px;color:var(--white);display:flex;align-items:center;justify-content:center;font:700 16px "Lato",sans-serif}
.kid-card{top:978px;width:188px}
.kid-card .ph{height:224px;background:linear-gradient(160deg,#8c7a6e,#4e4440)}
.kid-card dl{margin-top:22px;font:400 14px "Lato",sans-serif;color:var(--muted);line-height:29px}

/* bands */
.band{left:0;width:1200px;background:var(--sky)}
.framed{background:var(--white);padding:14px}
.framed .ph{width:100%;height:100%}
.about-text{left:640px;top:1643px;width:431px;font:400 13.5px/19px "Lato",sans-serif;color:var(--white)}
.step{top:2183px;width:300px;text-align:center}
.step h3{font:700 15px "Lato",sans-serif;color:var(--ink)}
.step p{font:400 12px/17px "Lato",sans-serif;color:var(--muted);margin-top:12px}
.faq{left:122px;top:2470px;width:443px;list-style:none}
.faq li{height:34px;border-bottom:1px solid rgba(255,255,255,.5);display:flex;align-items:center;justify-content:space-between;font:400 13.5px "Lato",sans-serif;color:var(--white)}
.faq li span:first-child::before{content:"";display:inline-block;width:12px;height:12px;border-radius:50%;background:var(--red);margin-right:12px;vertical-align:-1px}
.process-text{left:117px;top:2948px;width:552px;font:400 13.5px/19px "Lato",sans-serif;color:var(--ink)}
.process-text strong{display:block;text-align:center;color:var(--red);font-weight:700;margin-bottom:6px}
.phone{left:690px;top:3000px;width:332px;display:flex;align-items:center;justify-content:center;gap:14px;font:700 36px "Lato",sans-serif;color:var(--red);white-space:nowrap}

/* newsletter & footer */
.news{left:0;top:3232px;width:1200px;height:78px;background:var(--sky)}
.news h2{position:absolute;left:122px;top:24px;font:700 27px/30px "Lato",sans-serif;color:var(--white);letter-spacing:.5px;white-space:nowrap}
.news .input{position:absolute;left:636px;top:20px;width:318px;height:40px;background:var(--white);font:400 14px "Lato",sans-serif;color:#777;padding:11px 14px}
.news .btn{left:954px;top:20px;width:124px;height:40px;border-radius:0}
.footer{left:0;top:3310px;width:1200px;height:292px;background:var(--dark);color:var(--white)}
.footer h4{position:absolute;font:700 19px "Lato",sans-serif;text-transform:uppercase}
.footer h4::after{content:"";display:block;width:150px;height:1px;background:#888;margin-top:10px}
.footer p,.footer ul{position:absolute;font:400 12.5px/17px "Lato",sans-serif;list-style:none}
.bottom{left:0;top:3602px;width:1200px;height:49px;background:var(--sky);font:400 12px "Lato",sans-serif;color:var(--white);padding:17px 122px}
.chat{left:815px;top:3578px;width:263px;height:73px;background:var(--red);border-radius:6px 6px 0 0;display:flex;align-items:center;justify-content:center;gap:14px;font:700 28px "Lato",sans-serif;color:var(--white)}
</style>
</head>
<body>

<!-- Hero -->
<section class="abs hero">
  <nav class="abs nav"><span>Home</span><span>Missing Kids</span><span>About Seek The Youth</span><span>Contact</span><span>FAQ</span></nav>
  <div class="abs brand"><span class="dot"></span>Autos For Youth</div>
  <h1 class="abs headline">Donate Your Car!</h1>
  <p class="abs subhead">HELP FIND MISSING KIDS</p>
  <div class="abs mini-brand"><span class="sq"></span>Seek The Youth</div>
  <ul class="abs perks">
    <li>• Fast Free Pickup - 24hr Response</li>
    <li>• Tax Deduction - Easy To Do!</li>
    <li>• No Emission Test Required</li>
  </ul>
  <span class="btn" style="left:185px;top:499px;width:155px;height:46px">Leran More</span>
  <span class="btn" style="left:368px;top:499px;width:167px;height:46px">Missing Kids</span>

  <form class="abs form">
    <h2>Donate Your Car Online</h2>
    <p>Fill out the form &amp; help protect the future of children.</p>
    <div class="row"><span class="field">First Name</span><span class="field">Last Name</span></div>
    <div class="row"><span class="field">Phone No</span><span class="field">Zip Dode</span></div>
    <div class="row"><span class="field">E-Mail Address</span></div>
    <div class="row"><span class="field">Choose Year <b>▾</b></span><span class="field">Choose Make <b>▾</b></span></div>
    <div class="row"><span class="field">Vehicle Model</span></div>
    <span class="btn">Donate Now</span>
  </form>
</section>
<svg class="abs wave" width="1200" height="100" viewBox="0 0 1200 100" aria-hidden="true"><path d="M0 40 Q600 140 1200 30 L1200 100 L0 100 Z" fill="#ffffff"/></svg>
<div class="abs kids" role="img" aria-label="Four smiling children lying on their stomachs with hands on cheeks"></div>

<!-- Missing kids -->
<div class="tag orange" style="left:480px;top:862px;width:240px;height:56px">Missing Kids</div>
<div class="abs" style="left:1017px;top:873px;display:flex;gap:7px">
  <span class="arrow-btn" style="background:var(--pink)">‹</span>
  <span class="arrow-btn" style="background:var(--sky)">›</span>
</div>
<article class="abs kid-card" style="left:122px"><div class="ph" role="img" aria-label="Portrait of missing child Malik Turner"></div>
  <dl><dt>Name:&nbsp; Malik Turner</dt><dt>City:&nbsp; Los Angeles</dt><dt>DOB:&nbsp; 03/21/2009</dt><dt>ABD:&nbsp; 06/13/2013</dt></dl></article>
<article class="abs kid-card" style="left:380px"><div class="ph" role="img" aria-label="Portrait of missing child Rosa Delgado" style="background:linear-gradient(160deg,#c9c9c9,#7a7a7a)"></div>
  <dl><dt>Name:&nbsp; Rosa Delgado</dt><dt>City:&nbsp; Los Beach</dt><dt>DOB:&nbsp; 05/30/2004</dt><dt>ABD:&nbsp; 12/26/2013</dt></dl></article>
<article class="abs kid-card" style="left:635px"><div class="ph" role="img" aria-label="Portrait of missing child Nia Castillo" style="background:linear-gradient(160deg,#8db7d6,#c49a8a)"></div>
  <dl><dt>Name:&nbsp; Nia Castillo</dt><dt>City:&nbsp; Pico Rivera</dt><dt>DOB:&nbsp; 01/30/2002</dt><dt>ABD:&nbsp; 02/13/2003</dt></dl></article>
<article class="abs kid-card" style="left:891px"><div class="ph" role="img" aria-label="Portrait of missing child Greta Holm" style="background:linear-gradient(160deg,#9a7358,#4a3020)"></div>
  <dl><dt>Name:&nbsp; Greta Holm</dt><dt>City:&nbsp; Bell Gardens</dt><dt>DOB:&nbsp; 11/20/2000</dt><dt>ABD:&nbsp; 12/17/2015</dt></dl></article>
<span class="btn" style="left:518px;top:1375px;width:168px;height:42px">View All</span>

<!-- About -->
<section class="abs band" style="top:1490px;height:457px"></section>
<div class="abs framed" style="left:122px;top:1529px;width:462px;height:357px"><div class="ph" role="img" aria-label="Many cupped hands holding coins together" style="background:linear-gradient(135deg,#8a6a55,#3c3a44)"></div></div>
<div class="tag green" style="left:628px;top:1538px;width:419px;height:59px">About Seek The Youth</div>
<p class="abs about-text">Seek The Youth is a non-profit corporation dedicated to the recovery of missing children and to the prevention of the abuse and endangerment of children. Seek The Youth assists families searching for missing children by helping them to access local and federal law enforcement, advising them on the appropriate legal documents, and connecting them with other non-profit organizations or community resources that may help them in their search for their children.</p>
<span class="btn" style="left:640px;top:1813px;width:166px;height:44px">Learn More</span>

<!-- How to donate -->
<div class="tag orange" style="left:452px;top:1991px;width:296px;height:61px">How To Donate</div>
<svg class="abs" style="left:230px;top:2080px" width="740" height="90" viewBox="0 0 740 90" aria-hidden="true">
  <path d="M70 50 Q200 95 330 55" fill="none" stroke="#1c3a6e" stroke-width="6" stroke-dasharray="0 14" stroke-linecap="round"/>
  <path d="M410 45 Q550 -5 660 45" fill="none" stroke="#1c3a6e" stroke-width="6" stroke-dasharray="0 14" stroke-linecap="round"/>
  <rect x="14" y="14" width="40" height="54" rx="3" fill="#fff" stroke="#333" stroke-width="3"/>
  <rect x="26" y="8" width="16" height="10" fill="#333"/>
  <circle cx="34" cy="40" r="7" fill="#3aa9e6"/>
  <path d="M345 50 l10 -14 h38 l12 14 h8 v14 h-76 v-14 z" fill="#6b8fd6" stroke="#333" stroke-width="2"/>
  <circle cx="360" cy="66" r="6" fill="#333"/><circle cx="400" cy="66" r="6" fill="#333"/>
  <path d="M670 40 l20 -10 l18 12 l20 -10 M680 48 l14 12 h12 l16 -14" fill="none" stroke="#333" stroke-width="4" stroke-linecap="round" stroke-linejoin="round"/>
</svg>
<div class="abs step" style="left:113px"><h3>Fill Out a Form</h3><p>Submit Your Car's Info Online with a<br>simple Donations Form</p></div>
<div class="abs step" style="left:446px"><h3>Arrange a Pickup</h3><p>we'll call you within 24 hours to arrange a<br>free pickup for your vehicle</p></div>
<div class="abs step" style="left:775px"><h3>You Are Done!</h3><p>Receive a Tax Receipt<br>We Low Your car &amp; Proceed Help Kids.</p></div>

<!-- FAQ -->
<section class="abs band" style="top:2332px;height:450px"></section>
<div class="tag green" style="left:110px;top:2385px;width:445px;height:61px">Frequently Asked Questions</div>
<ul class="abs faq">
  <li><span>Why donate a vehicle or vessel?</span><span>+</span></li>
  <li><span>How do I donate a vehicle or vessel?</span><span>+</span></li>
  <li><span>How does my vehicle or vessel donation benefit the charity?</span><span>+</span></li>
  <li><span>How does donating a car or boat benefit my taxes?</span><span>+</span></li>
  <li><span>How long does it take to pickup my donation?</span><span>+</span></li>
  <li><span>What happens to my car after it's picked up?</span><span>+</span></li>
  <li><span>Do I have any liability after the vehicle/vessel is picked up?</span><span>+</span></li>
  <li><span>What kinds of donations can the charity accept?</span><span>+</span></li>
</ul>
<div class="abs framed" style="left:613px;top:2397px;width:458px;height:341px"><div class="ph" role="img" aria-label="Group of smiling kids giving thumbs up" style="background:linear-gradient(135deg,#f2a860,#c97a4a,#6a9ad0)"></div></div>

<!-- Process & call -->
<div class="tag orange" style="left:170px;top:2853px;width:397px;height:58px">Process Of The Search</div>
<div class="tag orange" style="left:725px;top:2853px;width:262px;height:58px">Call Us Today</div>
<p class="abs process-text"><strong>Case Management:</strong>Seek The Youth's case workers assists families of missing children by helping them through the process of obtaining custody orders, working with law enforcement, and connecting them with other nonprofit organizations or community resources that may also assist them in their search for their children. Seek The Youth also works in conjunction with the National Registry for Lost Youth.</p>
<span class="btn" style="left:195px;top:3115px;width:333px;height:44px">Donate Now to Elp Us Find a Child</span>
<p class="abs" style="left:725px;top:2950px;width:262px;text-align:center;font:400 14px 'Lato',sans-serif;color:var(--muted)">Live Operators Available - 7 Days A Week</p>
<div class="abs phone">
  <svg width="32" height="32" viewBox="0 0 24 24" aria-hidden="true"><path d="M6.6 10.8a15 15 0 0 0 6.6 6.6l2.2-2.2a1 1 0 0 1 1-.25 11.4 11.4 0 0 0 3.6.57 1 1 0 0 1 1 1V20a1 1 0 0 1-1 1A17 17 0 0 1 3 4a1 1 0 0 1 1-1h3.5a1 1 0 0 1 1 1c0 1.25.2 2.45.57 3.57a1 1 0 0 1-.25 1z" fill="#e8222f"/></svg>
  <span>888-555-0142</span>
</div>

<!-- Newsletter -->
<section class="abs news">
  <h2>SUBSCRIBE FOR OUR NEWSLETTER</h2>
  <span class="input">E-Mail Address</span>
  <span class="btn">Subscribe</span>
</section>

<!-- Footer -->
<footer class="abs footer">
  <div class="abs mini-brand" style="left:122px;top:50px;width:auto;text-align:left;font-size:14px"><span class="sq" style="margin:0 0 6px"></span>Seek The Youth</div>
  <p style="left:122px;top:112px;width:190px">Seek The Youth is a non-profit corporation dedicated to the recovery of missing children and to the prevention of the abuse and endangerment of children.</p>
  <p style="left:122px;top:210px">READ MORE...</p>
  <h4 style="left:453px;top:50px">Quick Link</h4>
  <ul style="left:453px;top:108px;line-height:24px"><li>Home</li><li>About Seek The Youth</li><li>Missing Kids</li><li>Contact</li><li>FAQ</li></ul>
  <h4 style="left:745px;top:50px">Privacy Policy</h4>
  <p style="left:745px;top:108px;width:335px">www.autosforyouth.net is not affiliated with Rides4Teens, RidesForTeens, WheelsForTeens, Wheels4Teens, United Lift Wheels For Teens, or any other website. Your donation to www.autosforyouth.net will benefit Seek The Youth, a registered Non Profit organization that helps find missing children. Seek The Youth is not affiliated with any other vehicle donation program.</p>
</footer>
<div class="abs bottom">© Autos For Youth 2016. All Rights Reserved</div>
<div class="abs chat">
  <svg width="34" height="30" viewBox="0 0 34 30" aria-hidden="true"><path d="M4 2h26a3 3 0 0 1 3 3v14a3 3 0 0 1-3 3H14l-8 7v-7H4a3 3 0 0 1-3-3V5a3 3 0 0 1 3-3z" fill="#fff"/></svg>
  LIVE CHAT
</div>

</body>
</html>
```